Packaged Food Business Needs a Packaging Design

We need a package design to be used as a label/sticker on the lids of round and square transparent plastic containers and on the sides of resealable stand-up pouches. The brand name is 'Tastora' - please find attached logo together with pictures of the sample containers and pouch. We will use the packaging to market a wide variety of food categories from nuts, dried fruits, spices, cooking chocolates, baking ingredients, cereals, grains and pulses.

OVERALL FEEDBACK ON DESIGNS ALREADY RECEIVED:

- We have found so far that a lot of our mandatory requirements are not adhered to in designs that have been submitted so far. We would like to emphasise that the ingredient, weight and expiry text will be printed at the time of packing so it should not take prime space on the pack BUT at the same time some 'blank' space needs to flawlessly be incorporated into the overall design for this purpose
- We encourage you to glorify the brand logo in the pack, and absolutely refrain from duplicating the tagline
- Please note that ONE label design will be used to pack a wide variety of food ingredients and therefore please ensure that the choice of your design incorporates this requirement, in the past we have received designs that are limited to only one type of food (like nuts) or have received designs that are too floral or leafy (and not grounded to food
- Please ensure that you submit designs for all three packaging formats, it is critical to see the family look from the on-set

Target Market(s)

The brand is targeting both mothers and professional chefs and therefore the label design should be broadly approachable and convey affordable premium

Industry/Entity Type

Business

Requirements
Must have
• - Consistent with the brand name and logo, the overall look and feel of the packaging should convey values of healthy, gourmet food ingredients, high in nourishment and project a sense of delightful taste
• - The design styling to be modern and 'simplistic' (embracing 'less-is-more' type of a design style)
• - Design a packaging architecture that incorporates the brand logo together with its tagline lock-up of 'savour the goodness in every morsel' - find logo attached
• - The design needs to have a dedicated area to print the ingredient (e.g., Mixed Nuts), weight (e.g., 500g) and expiry (this space needs to be flawlessly incorporated into the design) - this information will be printed either with an inkjet printer or with a rubber stamp so please leave an empty space (the text should not be part of the design, just the area for the text needs to be included in the design)
• - The packaging must include 'Packed By: Kelvane Distributors Ltd, P. O. Box 51946, Kampala - Uganda'
• - For the design of the resealable pouch, please incorporate a window to see through the ingredients and a hole on top to hang on supermarket pegs if necessary
Nice to have
• - We would love to have some design submissions that are bold and cheerful and fun (but not frivolous) - please see attached inspiration for 'fun' packaging. The attachments are purely for inspiration, not to infringe on anyone else's TM and copyrights
• - Incorporate green to convey healthy, organic values
• - Explore use of gold and silver convey premiumness
Should not have
• - Do not duplicate the tagline
• - Do not include the ingredient, weight and expiry in the main graphic of the design, these will be printed at the time of packing so ensure there is provision for this in a flawless way in the design (e.g., via a blank space allocated for this purpose)

```html
<!DOCTYPE html>
<html lang="en">
<head>
<meta charset="utf-8">
<title>Tastora Label Family</title>
<link rel="stylesheet" href="https://fonts.googleapis.com/css2?family=Oswald:wght@700&family=Arimo:wght@700&family=Didact+Gothic&display=swap">
<style>
  :root {
    --sky: #d4f3fc;
    --maroon: #800000;
    --maroon-deep: #560406;
    --cocoa: #3f2209;
    --leaf: #5a8a2e;
    --cream: #fde9b8;
    --gold: #f6cf3a;
    --ring: #000000;
    --paper: #ffffff;
  }
  html, body { margin: 0; padding: 0; width: 1200px; height: 1200px; overflow: hidden; background: var(--paper); }
  .label-sheet { display: block; width: 1200px; height: 1200px; }
  .sky { fill: var(--sky); }
  .maroon { fill: var(--maroon); }
  .maroon-deep { fill: var(--maroon-deep); }
  .print-field { fill: var(--paper); }
  .brand-name { font-family: "Oswald", "Arial Narrow", sans-serif; font-weight: 700; fill: var(--cocoa); letter-spacing: 0.06em; }
  .tagline { font-family: "Arimo", Arial, sans-serif; font-weight: 700; fill: var(--leaf); text-transform: uppercase; }
  .field-label { font-family: "Didact Gothic", Arial, sans-serif; fill: var(--cream); }
  .packer { font-family: "Didact Gothic", Arial, sans-serif; fill: var(--cream); letter-spacing: 0.03em; }
  .clean-note { font-family: "Arimo", Arial, sans-serif; font-weight: 700; fill: var(--gold); }
  .icon { fill: var(--gold); }
</style>
</head>
<body>
<svg class="label-sheet" viewBox="0 0 1500 1500" xmlns="http://www.w3.org/2000/svg">
  <defs>
    <clipPath id="round-face"><circle cx="425" cy="418" r="396"/></clipPath>
    <g id="clean-icons">
      <path class="icon" d="M0 14 L8 0 L16 14 Z M3 12 L8 4 L13 12 Z" fill-rule="evenodd"/>
      <path class="icon" d="M-2 16 H18 L14 22 H2 Z"/>
      <rect class="icon" x="34" y="6" width="14" height="18" rx="2"/>
      <rect class="icon" x="32" y="2" width="18" height="3"/>
      <circle class="icon" cx="54" cy="2" r="3"/>
      <path class="icon" d="M52 6 L57 6 L58 22 L54 22 Z"/>
    </g>
  </defs>

  <!-- Round lid label -->
  <g class="round-label">
    <g clip-path="url(#round-face)">
      <rect class="sky" x="0" y="0" width="850" height="345"/>
      <path class="maroon" d="M40 482 Q170 510 300 482 Q420 455 520 480 Q650 515 830 496 L830 830 L40 830 Z"/>
      <path class="maroon-deep" d="M55 383 H797 L790 503 Q640 512 500 472 Q330 428 150 496 Q70 492 55 465 Z"/>
    </g>
    <circle cx="425" cy="418" r="403" fill="none" stroke="var(--ring)" stroke-width="14"/>
    <text class="brand-name" x="100" y="335" font-size="150" textLength="655" lengthAdjust="spacingAndGlyphs">TASTORA</text>
    <text class="tagline" x="100" y="373" font-size="27" textLength="637" lengthAdjust="spacingAndGlyphs">Savour the goodness in every morsel!</text>
    <text class="packer" x="430" y="413" font-size="22" text-anchor="middle">Packed By: Kelvane Distributors Ltd</text>
    <text class="packer" x="430" y="438" font-size="22" text-anchor="middle">P. O. Box 51946, Kampala - Uganda</text>
    <text class="field-label" x="153" y="555" font-size="19">Expiry date</text>
    <rect class="print-field" x="260" y="537" width="178" height="25"/>
    <text class="field-label" x="498" y="553" font-size="19">Weight</text>
    <rect class="print-field" x="570" y="537" width="130" height="25"/>
    <text class="field-label" x="146" y="608" font-size="19">Packed date</text>
    <rect class="print-field" x="260" y="591" width="178" height="25"/>
    <text class="field-label" x="488" y="610" font-size="19">Price</text>
    <rect class="print-field" x="545" y="591" width="155" height="25"/>
    <text class="field-label" x="425" y="645" font-size="19" text-anchor="middle">Ingredients</text>
    <rect class="print-field" x="236" y="654" width="387" height="62"/>
    <use href="#clean-icons" x="293" y="738"/>
    <text class="clean-note" x="362" y="757" font-size="17">Keep your country clean.</text>
  </g>

  <!-- Square lid label -->
  <g class="square-label">
    <rect class="sky" x="880" y="82" width="480" height="250"/>
    <text class="brand-name" x="888" y="322" font-size="100" textLength="464" lengthAdjust="spacingAndGlyphs">TASTORA</text>
    <text class="tagline" x="887" y="349" font-size="20" textLength="454" lengthAdjust="spacingAndGlyphs">Savour the goodness in every morsel!</text>
    <path class="maroon" d="M880 356 H1100 Q1140 470 1200 510 Q1260 545 1358 547 V688 Q1290 680 1200 660 Q1110 640 1010 665 Q930 672 880 655 Z"/>
    <path class="maroon-deep" d="M880 662 Q950 684 1030 670 Q1110 642 1200 668 Q1290 697 1358 702 V790 H880 Z"/>
    <text class="field-label" x="900" y="396" font-size="19">Weight</text>
    <rect class="print-field" x="1014" y="380" width="98" height="25"/>
    <text class="field-label" x="897" y="441" font-size="19">Price</text>
    <rect class="print-field" x="1015" y="423" width="108" height="25"/>
    <text class="field-label" x="893" y="485" font-size="19">Expiry date</text>
    <rect class="print-field" x="1015" y="467" width="134" height="25"/>
    <text class="field-label" x="894" y="527" font-size="19">Packed date</text>
    <rect class="print-field" x="1015" y="510" width="134" height="25"/>
    <text class="field-label" x="891" y="576" font-size="21">Ingredients</text>
    <rect class="print-field" x="1023" y="560" width="320" height="71"/>
    <text class="packer" x="1125" y="725" font-size="22" text-anchor="middle">Packed By: Kelvane Distributors Ltd</text>
    <text class="packer" x="1124" y="749" font-size="22" text-anchor="middle">P. O. Box 51946, Kampala - Uganda</text>
    <use href="#clean-icons" x="985" y="759"/>
    <text class="clean-note" x="1053" y="778" font-size="17">Keep your country clean.</text>
  </g>

  <!-- Stand-up pouch label -->
  <g class="pouch-label">
    <path class="sky" d="M174 848 H712 L1000 1128 H174 Z"/>
    <path class="maroon" d="M752 848 H1163 V1247 L1150 1236 V862 H766 Z"/>
    <text class="brand-name" x="200" y="1118" font-size="150" textLength="645" lengthAdjust="spacingAndGlyphs">TASTORA</text>
    <text class="tagline" x="198" y="1156" font-size="27" textLength="628" lengthAdjust="spacingAndGlyphs">Savour the goodness in every morsel!</text>
    <path class="maroon" d="M174 1164 H1040 L1163 1284 V1488 H174 Z"/>
    <text class="field-label" x="324" y="1214" font-size="26">Weight</text>
    <rect class="print-field" x="455" y="1197" width="135" height="31"/>
    <text class="field-label" x="612" y="1217" font-size="28">Expiry date</text>
    <rect class="print-field" x="783" y="1192" width="185" height="34"/>
    <text class="field-label" x="328" y="1272" font-size="26">Price</text>
    <rect class="print-field" x="440" y="1247" width="150" height="31"/>
    <text class="field-label" x="613" y="1274" font-size="28">Packed date</text>
    <rect class="print-field" x="783" y="1251" width="185" height="34"/>
    <text class="field-label" x="640" y="1315" font-size="25" text-anchor="middle">Ingredients</text>
    <rect class="print-field" x="426" y="1325" width="444" height="84"/>
    <text class="packer" x="453" y="1444" font-size="28" text-anchor="middle">Packed By: Kelvane Distributors Ltd</text>
    <text class="packer" x="451" y="1473" font-size="28" text-anchor="middle">P. O. Box 51946, Kampala - Uganda</text>
    <use href="#clean-icons" x="738" y="1433" transform="translate(-275 -503) scale(1.37)"/>
    <text class="clean-note" x="833" y="1462" font-size="24">Keep your country clean.</text>
  </g>
</svg>
</body>
</html>
```